Swimming Pool Supply Company Business Cards

We need business cards designed for company. These need to be easy to edit so that we can fill in names, titles, and contact info for each person who works here.

Dalton R. Pembry
Manager of Legal & Finance
J.L. Pembry, Incorporated

4837 Grelwood Avenue
Marlow Crossing, PA 19054

E. dalton@jlpembry.com
M. (215) 555-7193
O. (215) 555-4620

Contact Information for Business Card

Looking to upgrade current business cards with graphic that can be edited. Looking for fresh ideas for an age old industry.

Font styles to use
Serif
Sans Serif

Colors

Designer to choose colors to be used in the design.

Requirements
Must have
• Professional, fresh, unique but professional

```html
<!DOCTYPE html>
<html lang="en">
<head>
<meta charset="utf-8">
<title>J.L. Pembry Business Card</title>
<link href="https://fonts.googleapis.com/css2?family=Nunito+Sans:wght@400;700;800&display=swap" rel="stylesheet">
<style>
  :root {
    --page-bg: #e6e2dd;
    --card-bg: #f3f5f7;
    --name-blue: #1f4f9a;
    --body-grey: #3d3f44;
    --icon-blue: #2a5ea8;
    --navy: #17407a;
    --teal: #2a7fa6;
    --teal-light: #7fb5cf;
    --rose: #eac4c2;
    --tagline-rose: #cf8a8e;
  }
  * { margin: 0; padding: 0; box-sizing: border-box; }
  html, body {
    width: 1200px; height: 970px; overflow: hidden;
    background: var(--page-bg);
    font-family: "Nunito Sans", Arial, sans-serif;
  }
  .business-card {
    position: absolute; left: 100px; top: 205px;
    width: 1000px; height: 560px;
    border-radius: 42px; overflow: hidden;
    background: var(--card-bg);
    box-shadow: 0 14px 40px rgba(0,0,0,0.18);
  }
  .card-wave { position: absolute; inset: 0; }
  .person-name {
    position: absolute; left: 81px; top: 78px;
    font-size: 37px; font-weight: 800; color: var(--name-blue);
    letter-spacing: 0.2px; white-space: nowrap;
  }
  .person-title {
    position: absolute; left: 82px; top: 120px;
    font-size: 21px; color: var(--body-grey); white-space: nowrap;
  }
  .company-address {
    position: absolute; left: 82px; top: 200px;
    font-size: 21px; line-height: 31.5px; color: var(--body-grey);
    list-style: none; white-space: nowrap;
  }
  .contact-phones {
    position: absolute; left: 452px; top: 231.5px;
    font-size: 21px; line-height: 31.5px; color: var(--body-grey);
    list-style: none; white-space: nowrap;
  }
  .contact-phones li { display: flex; align-items: center; gap: 16px; }
  .contact-phones svg { width: 20px; height: 20px; }
  .brand-name {
    position: absolute; left: 53px; top: 436px;
    font-size: 80px; font-weight: 800; color: var(--rose);
    letter-spacing: 2px; line-height: 1;
  }
  .brand-tagline {
    position: absolute; left: 484px; top: 470px;
    font-size: 21px; font-weight: 700; color: var(--tagline-rose);
    white-space: nowrap;
  }
</style>
</head>
<body>
  <div class="business-card">
    <svg class="card-wave" width="1000" height="560" viewBox="0 0 1000 560" aria-hidden="true">
      <defs>
        <linearGradient id="band-fill" x1="0" y1="0" x2="1" y2="0.4">
          <stop offset="0" stop-color="#2f86ad"/>
          <stop offset="0.55" stop-color="#1f6597"/>
          <stop offset="1" stop-color="#18477f"/>
        </linearGradient>
        <linearGradient id="band-lower" x1="0" y1="0" x2="0" y2="1">
          <stop offset="0" stop-color="#2b7aa3" stop-opacity="0.9"/>
          <stop offset="1" stop-color="#1d5c8f"/>
        </linearGradient>
      </defs>
      <path d="M0,425 C120,370 220,345 300,350 C420,358 520,405 640,402 C780,398 900,280 1000,117 L1000,560 L0,560 Z" fill="var(--navy)"/>
      <path d="M0,432 C130,385 230,368 320,373 C440,380 540,420 650,418 C790,414 910,300 1000,160 L1000,560 L0,560 Z" fill="var(--teal-light)"/>
      <path d="M0,440 C140,395 240,380 330,385 C450,392 550,432 660,430 C800,426 915,315 1000,185 L1000,560 L0,560 Z" fill="url(#band-fill)"/>
      <path d="M0,470 C200,430 420,445 620,455 C800,462 930,420 1000,380 L1000,560 L0,560 Z" fill="url(#band-lower)" opacity="0.55"/>
    </svg>

    <h1 class="person-name">Dalton R. Pembry</h1>
    <p class="person-title">Manager of Legal &amp; Finance</p>

    <ul class="company-address">
      <li>J.L. Pembry, Incorporated</li>
      <li>4837 Grelwood Avenue</li>
      <li>Marlow Crossing, PA 19054</li>
    </ul>

    <ul class="contact-phones">
      <li>
        <svg viewBox="0 0 20 20" aria-label="Mobile"><rect x="5" y="1.5" width="10" height="17" rx="1.8" fill="none" stroke="var(--icon-blue)" stroke-width="2"/><line x1="8.5" y1="15" x2="11.5" y2="15" stroke="var(--icon-blue)" stroke-width="1.6"/></svg>
        <span>(215) 555-7193</span>
      </li>
      <li>
        <svg viewBox="0 0 20 20" aria-label="Office"><path d="M5 2 L8 2 L9.5 6 L7.5 7.5 C8.5 10 10 11.5 12.5 12.5 L14 10.5 L18 12 L18 15 C18 16.5 16.5 18 15 18 C8 17.5 2.5 12 2 5 C2 3.5 3.5 2 5 2 Z" fill="var(--icon-blue)"/></svg>
        <span>(215) 555-4620</span>
      </li>
    </ul>

    <div class="brand-name">PEMBRY</div>
    <p class="brand-tagline">Crystal Clear Pools, Backed By People Who Care</p>
  </div>
</body>
</html>
```